Business Card Design Project - Tall Maple

We are looking for a new business card design. Our company name is Tall Maple Communication Solutions. Our primary function is to provide our clients with communication solutions. These solutions include commercial phone systems and T1 and Fiber Internet lines. Another major part of the business is cabling new buildings with CAT5 cable for both data and phone.

Industry/Entity Type

Communication

Requirements
Must have
• The cards need to be two sided and have some bleeding edge color.
Nice to have
• We are going to upload our current logo BUT we are not married to this logo. If you want to incorporate a re-designed logo with the new business card - please feel free to do so. We are looking for a new bold look that is very colorful yet professional.

```html
<!DOCTYPE html>
<html lang="en">
<head>
<meta charset="utf-8">
<title>Tall Maple Communication Solutions — Business Card</title>
<link rel="stylesheet" href="https://fonts.googleapis.com/css2?family=Source+Sans+3:wght@400&display=swap">
<style>
  :root {
    --navy: #062d63;
    --white: #ffffff;
    --backdrop: #ece7e1;
    --text-font: "Source Sans 3", sans-serif;
  }
  * { margin: 0; padding: 0; box-sizing: border-box; }
  html, body {
    width: 1066px; height: 1200px; overflow: hidden;
    background: var(--backdrop);
  }
  .canvas { position: relative; width: 1066px; height: 1200px; }
  .card {
    position: absolute; left: 127px; width: 786px; height: 506px;
    background: var(--navy); overflow: hidden;
    font-family: var(--text-font);
  }
  .card--front { top: 60px; }
  .card--back { top: 642px; height: 508px; }

  .front-band {
    position: absolute; left: 0; right: 0; top: 157px; height: 189px;
    background: var(--white);
    display: flex; align-items: center; justify-content: center;
  }
  .back-arc { position: absolute; inset: 0; }

  .company-name {
    color: var(--navy); font-weight: 400; white-space: nowrap; line-height: 1;
  }
  .card--front .company-name { font-size: 40px; }
  .card--back .company-name {
    position: absolute; left: 0; right: 0; top: 108px;
    text-align: center; font-size: 32px;
  }

  .contact { position: absolute; color: var(--white); font-weight: 400; }
  .person-name { left: 41px; top: 318px; font-size: 32px; line-height: 1.2; }
  .address { left: 41px; top: 424px; font-size: 20px; line-height: 28px; font-style: normal; }
  .phones { left: 551px; top: 372px; font-size: 20px; line-height: 28px; list-style: none; }
</style>
</head>
<body>
<main class="canvas">
  <section class="card card--front" aria-label="Card front">
    <div class="front-band">
      <p class="company-name">Tall Maple Communication Solutions</p>
    </div>
  </section>

  <section class="card card--back" aria-label="Card back">
    <svg class="back-arc" width="786" height="508" viewBox="0 0 786 508" aria-hidden="true">
      <circle cx="395" cy="-154" r="419" fill="#ffffff"/>
    </svg>
    <p class="company-name">Tall Maple Communication Solutions</p>
    <h1 class="contact person-name">Reid Halvorsen</h1>
    <address class="contact address">
      1840 W Larkspur Avenue, Suite 410<br>
      Sandvale, AZ 85099
    </address>
    <ul class="contact phones">
      <li>Office: 555.214.0190</li>
      <li>Cell: 555.306.4471</li>
      <li>24/7: 555.918.2036</li>
      <li>Fax: 555.427.6682</li>
    </ul>
  </section>
</main>
</body>
</html>
```